Employee I.D. Card - Badge

We need an employee I.D. card designed. Our employees are going to be wearing these. I would like to have it look nice. Something professional yet cool (not uptight if that makes sense).
Project Scope:
Vertical orientation
Company name ------------- (Bright and Tidy)
Website ------------- (brightandtidymn.example)
Employee Picture
background check image
front and back designed - same design on either side
You can create the card without having the employee images on them.
Here are the dimensions -
2.125 x 3.370 inches
Double sided - same design can be used front and back
Background badge - I would like to add an image that shows that the employee has taken a background check. I've added the press-kit for the company we use. If you have a better idea than incorporating their logo, we can certainly do something different.
Example image-
https://www.findwell-search.example/results?q=background+check+badge&mode=images
The print company will set up the names.
Logo is attached
Also attached are our business cards. You can use this for an idea of brand/company style.
Our website - brightandtidymn.example

```html
<!DOCTYPE html>
<html lang="en">
<head>
<meta charset="utf-8">
<title>Bright and Tidy – Employee ID Badge</title>
<link rel="stylesheet" href="https://fonts.googleapis.com/css2?family=Montserrat:wght@600;700&family=Roboto+Condensed:wght@700&display=swap">
<style>
  :root {
    --page-bg: #c2e8e0;
    --white: #ffffff;
    --brand-blue: #1a7cc8;
    --blue-light: #0ea3e2;
    --blue-deep: #0b68bb;
    --lime: #c9dc12;
    --lime-deep: #9cc41c;
    --silver: #d7d9dc;
    --photo-fill: #eeeff1;
    --gold: #d9b24a;
    --gold-dark: #2a2a2a;
  }
  * { margin: 0; padding: 0; box-sizing: border-box; }
  html, body { width: 1200px; height: 1031px; overflow: hidden; }
  body {
    background: var(--page-bg);
    position: relative;
    font-family: "Montserrat", sans-serif;
  }
  .badge-card {
    position: absolute;
    top: 173px;
    width: 462px;
    height: 686px;
    background: var(--white);
    overflow: hidden;
  }
  .badge-card--front { left: 86px; }
  .badge-card--back { left: 654px; }
  .card-art { position: absolute; inset: 0; width: 100%; height: 100%; }
  .brand-name {
    position: absolute;
    top: 46px;
    left: 0;
    width: 100%;
    text-align: center;
    font-family: "Montserrat", sans-serif;
    font-weight: 600;
    font-size: 50px;
    line-height: 58px;
    letter-spacing: -1px;
    color: var(--brand-blue);
  }
  .employee-name {
    position: absolute;
    top: 446px;
    left: 0;
    width: 100%;
    text-align: center;
    font-family: "Roboto Condensed", sans-serif;
    font-weight: 700;
    font-size: 42px;
    letter-spacing: 3px;
    color: var(--white);
  }
  .employee-title {
    position: absolute;
    top: 516px;
    left: 0;
    width: 100%;
    text-align: center;
    font-weight: 600;
    font-size: 19px;
    letter-spacing: 1.2px;
    color: var(--white);
  }
  .website {
    position: absolute;
    top: 597px;
    left: 40px;
    font-weight: 700;
    font-size: 18px;
    letter-spacing: 0.6px;
    color: var(--lime);
  }
  .website__tld { color: var(--white); }
</style>
</head>
<body>

<article class="badge-card badge-card--front">
  <svg class="card-art" viewBox="0 0 462 686" aria-hidden="true">
    <defs>
      <linearGradient id="blueField-a" x1="0" y1="0" x2="1" y2="1">
        <stop offset="0" stop-color="var(--blue-light)"/>
        <stop offset="1" stop-color="var(--blue-deep)"/>
      </linearGradient>
      <linearGradient id="limeSwoosh-a" x1="0" y1="0" x2="1" y2="0">
        <stop offset="0" stop-color="var(--lime)"/>
        <stop offset="1" stop-color="var(--lime-deep)"/>
      </linearGradient>
    </defs>
    <path class="swoosh-lime" d="M0,92 C70,210 190,290 300,296 C370,300 420,280 462,254 L462,292 C380,318 300,328 230,320 C150,310 70,280 0,240 Z" fill="url(#limeSwoosh-a)"/>
    <path class="swoosh-silver" d="M0,200 C80,260 170,300 260,318 C340,330 410,320 462,300 L462,312 C400,330 320,338 240,328 C150,316 70,290 0,262 Z" fill="var(--silver)"/>
    <path class="blue-field" d="M0,255 C90,300 170,322 250,330 C340,338 410,325 462,308 L462,686 L0,686 Z" fill="url(#blueField-a)"/>
    <circle class="photo-ring" cx="231" cy="314" r="108" fill="var(--brand-blue)"/>
    <circle class="photo-slot" cx="231" cy="314" r="103" fill="var(--photo-fill)" role="img" aria-label="Employee photo"/>
    <g class="dots">
      <circle cx="95" cy="240" r="4" fill="var(--lime-deep)"/>
      <circle cx="38" cy="247" r="3" fill="#bbbbbb"/>
      <circle cx="418" cy="366" r="4.5" fill="var(--lime)"/>
      <circle cx="358" cy="401" r="4" fill="#38b6f0"/>
      <circle cx="131" cy="419" r="4" fill="var(--lime)"/>
      <circle cx="415" cy="515" r="5.5" fill="var(--lime)"/>
      <circle cx="40" cy="567" r="7" fill="var(--lime)"/>
      <circle cx="303" cy="558" r="3.5" fill="#c8c8c8"/>
      <circle cx="140" cy="648" r="5" fill="#c8c8c8"/>
    </g>
    <g class="clearance-seal" role="img" aria-label="Background check cleared seal">
      <circle cx="388" cy="610" r="56" fill="var(--gold)"/>
      <circle cx="388" cy="610" r="46" fill="var(--gold-dark)"/>
      <circle cx="388" cy="610" r="22" fill="var(--gold)"/>
      <path d="M377,610 L385,619 L400,600" fill="none" stroke="var(--gold-dark)" stroke-width="5" stroke-linecap="round" stroke-linejoin="round"/>
    </g>
  </svg>
  <div class="brand-name">Bright<br>and Tidy</div>
  <h1 class="employee-name">JORDAN ELLIS</h1>
  <p class="employee-title">Managing Director</p>
  <p class="website">brightandtidymn<span class="website__tld">.example</span></p>
</article>

<article class="badge-card badge-card--back">
  <svg class="card-art" viewBox="0 0 462 686" aria-hidden="true">
    <defs>
      <linearGradient id="blueField-b" x1="0" y1="0" x2="1" y2="1">
        <stop offset="0" stop-color="var(--blue-light)"/>
        <stop offset="1" stop-color="var(--blue-deep)"/>
      </linearGradient>
      <linearGradient id="limeSwoosh-b" x1="0" y1="0" x2="1" y2="0">
        <stop offset="0" stop-color="var(--lime)"/>
        <stop offset="1" stop-color="var(--lime-deep)"/>
      </linearGradient>
    </defs>
    <path class="swoosh-lime" d="M0,92 C70,210 190,290 300,296 C370,300 420,280 462,254 L462,292 C380,318 300,328 230,320 C150,310 70,280 0,240 Z" fill="url(#limeSwoosh-b)"/>
    <path class="swoosh-silver" d="M0,200 C80,260 170,300 260,318 C340,330 410,320 462,300 L462,312 C400,330 320,338 240,328 C150,316 70,290 0,262 Z" fill="var(--silver)"/>
    <path class="blue-field" d="M0,255 C90,300 170,322 250,330 C340,338 410,325 462,308 L462,686 L0,686 Z" fill="url(#blueField-b)"/>
    <circle class="photo-ring" cx="231" cy="314" r="108" fill="var(--brand-blue)"/>
    <circle class="photo-slot" cx="231" cy="314" r="103" fill="var(--photo-fill)" role="img" aria-label="Employee photo"/>
    <g class="dots">
      <circle cx="95" cy="240" r="4" fill="var(--lime-deep)"/>
      <circle cx="38" cy="247" r="3" fill="#bbbbbb"/>
      <circle cx="418" cy="366" r="4.5" fill="var(--lime)"/>
      <circle cx="358" cy="401" r="4" fill="#38b6f0"/>
      <circle cx="131" cy="419" r="4" fill="var(--lime)"/>
      <circle cx="415" cy="515" r="5.5" fill="var(--lime)"/>
      <circle cx="40" cy="567" r="7" fill="var(--lime)"/>
      <circle cx="303" cy="558" r="3.5" fill="#c8c8c8"/>
      <circle cx="140" cy="648" r="5" fill="#c8c8c8"/>
    </g>
    <g class="clearance-seal" role="img" aria-label="Background check cleared seal">
      <circle cx="388" cy="610" r="56" fill="var(--gold)"/>
      <circle cx="388" cy="610" r="46" fill="var(--gold-dark)"/>
      <circle cx="388" cy="610" r="22" fill="var(--gold)"/>
      <path d="M377,610 L385,619 L400,600" fill="none" stroke="var(--gold-dark)" stroke-width="5" stroke-linecap="round" stroke-linejoin="round"/>
    </g>
  </svg>
  <div class="brand-name">Bright<br>and Tidy</div>
  <h2 class="employee-name">JORDAN ELLIS</h2>
  <p class="employee-title">Managing Director</p>
  <p class="website">brightandtidymn<span class="website__tld">.example</span></p>
</article>

</body>
</html>
```